International Vacuum Business Needs Brochure Design

We need a flyer 8 1/2" x 11" booklet style (folded in half) flyer design for a new company based in Toronto called "Swivo-Lux". We will be selling and installing a proprietary central vacuum system that is one of a kind to the condominium market mainly through various large builders throughout the country as well as a second distribution chain at a retail level. Our product has a very unique retractable hose system that allows the hose to be stored away within the walls of a space all by the push of a button. "No more hoses laying around the house" The design should communicate the following terms " sleek, discreet, convenient, sophisticated, modern"
Updates
Reason: Hello All,
I have extended the deadline by a few days so i can spend some time reviewing all the designs and try to finalize a decision.
Thank you for all the designs!!
Target Market(s)
Our target market is male/female aged 25-65, more so focussing on 25-50.
Industry/Entity Type
Retail
Requirements
Must have
- The brochure must have an amazing, really catchy front cover, demonstrating our logo and the unit we sell. Back page should have all our contact information and once again a product picture. The Pelm Ovra symbol should be smaller than our logo and on the inner pages of the brochure, not on the front
Our address and contact information as below
Swivo-Lux Inc.
517 Harnett Ave.
Kelvale, ON
K7P2R9
Office 555.203.6614
Fax 555.718.2093
Toll 555.346.8120
www.swivolux.example
Nice to have
- I would like to see a picture of a clean modern space possibly in a condominium looking out to a great view. Want to send that message that this unit can make your life relaxed and easy. Must have for every condominium space.
New age of vacuuming!!
Innovation
Should not have
- A traditional feel to it.

```html
<!DOCTYPE html>
<html lang="en">
<head>
<meta charset="utf-8">
<title>Swivo-Lux Brochure</title>
<link rel="stylesheet" href="https://fonts.googleapis.com/css2?family=Titillium+Web:wght@400;600;700&display=swap">
<style>
  :root{
    --red:#c4161c;
    --red-dark:#8e0f14;
    --charcoal:#2a2a2c;
    --silver:#d9dadc;
    --silver-light:#f1f1f2;
    --ink:#4a4a4d;
    --white:#ffffff;
    --backdrop:#e9e9e8;
  }
  *{box-sizing:border-box;margin:0;padding:0}
  html,body{width:1200px;height:900px;overflow:hidden;background:var(--backdrop);font-family:"Titillium Web",Arial,sans-serif}
  .page{position:absolute;top:172px;width:360px;height:556px;overflow:hidden;background:var(--white);box-shadow:0 4px 18px rgba(0,0,0,.18)}
  .cover{left:40px}
  .spread-left{left:440px}
  .spread-right{left:800px;box-shadow:4px 4px 18px rgba(0,0,0,.18)}
  .photo{position:absolute}

  /* cover */
  .cover-photo{left:0;top:0;width:360px;height:320px;background:linear-gradient(135deg,#d8d2c8 0%,#b49a86 45%,#7d8a95 100%)}
  .cover-band{position:absolute;left:0;top:0;width:360px;height:556px}
  .cover-headline{position:absolute;left:0;top:338px;width:360px;text-align:center;color:var(--white);font-weight:700;font-size:19.5px;line-height:23px;text-transform:uppercase;letter-spacing:.3px;text-shadow:0 2px 3px rgba(0,0,0,.35)}
  .cover-footer-photo{left:0;top:470px;width:150px;height:60px;background:linear-gradient(90deg,#cfd1d4,#9ea2a8)}
  .brand-box{position:absolute;display:flex;align-items:center;gap:8px;background:var(--charcoal);color:var(--white);font-weight:400;font-size:21px;letter-spacing:.5px;padding-left:14px}
  .brand-box .mark{width:16px;height:16px;background:var(--white)}
  .cover .brand-box{left:150px;top:470px;width:210px;height:60px}
  .cover-strip{position:absolute;left:0;top:530px;width:360px;height:26px;background:var(--red)}

  /* inner pages */
  .floor-photo{left:0;top:0;width:360px;height:200px;background:linear-gradient(160deg,#eef0f2 0%,#b8bcc0 50%,#5a3a2a 100%)}
  .unit-photo{left:0;top:0;width:360px;height:165px;background:linear-gradient(135deg,#f3f1ec 0%,#d7d2c6 55%,#8c8f92 100%)}
  .silver-sweep{position:absolute;left:0;top:0;width:360px;height:556px}
  .label{position:absolute;background:var(--red);color:var(--white);font-weight:600;font-size:27px;line-height:38px;padding:0 14px;text-transform:uppercase;box-shadow:0 3px 5px rgba(0,0,0,.25)}
  .copy{position:absolute;color:var(--ink);font-size:11.2px;line-height:15px}
  .label-simple{left:26px;top:222px}
  .copy-simple{left:26px;top:270px;width:312px}
  .label-convenience{left:26px;top:352px}
  .copy-convenience{left:26px;top:400px;width:312px}
  .page-band{position:absolute;left:0;bottom:0;width:360px;height:70px}

  .product-name{position:absolute;left:232px;top:180px;display:flex;align-items:center;gap:6px;background:var(--white);padding:8px 10px;font-size:15px;font-weight:700;color:var(--charcoal);box-shadow:0 2px 5px rgba(0,0,0,.2)}
  .product-name .mark{width:12px;height:12px;background:var(--red)}
  .label-demand{left:22px;top:232px}
  .copy-demand{left:22px;top:282px;width:318px}
  .copy-vision{left:22px;top:352px;width:318px}
  .specs{left:22px;top:440px;width:200px}
  .spread-right .brand-box{left:180px;top:464px;width:180px;height:46px;font-size:18px}
</style>
</head>
<body>

<section class="page cover" aria-label="Front cover">
  <div class="photo cover-photo" role="img" aria-label="Photo of a smiling family relaxing together on a clean living room floor"></div>
  <svg class="cover-band" viewBox="0 0 360 556" aria-hidden="true">
    <defs>
      <linearGradient id="coverRed" x1="0" y1="0" x2="0" y2="1">
        <stop offset="0" stop-color="#d21e24"/>
        <stop offset="1" stop-color="#9c1116"/>
      </linearGradient>
    </defs>
    <polygon points="0,320 30,320 60,295 90,320 360,310 360,470 0,470" fill="url(#coverRed)"/>
    <polyline points="0,322 30,322 60,297 90,322 360,312" fill="none" stroke="#ffffff" stroke-width="4"/>
  </svg>
  <h1 class="cover-headline">The most<br>sleek and discreet way<br>to have a clean<br>environment<br>for your family</h1>
  <div class="photo cover-footer-photo" role="img" aria-label="Photo of a person vacuuming a sofa with a central vacuum hose"></div>
  <div class="brand-box"><span class="mark"></span>Swivo-Lux</div>
  <div class="cover-strip"></div>
</section>

<section class="page spread-left" aria-label="Inside left page">
  <div class="photo floor-photo" role="img" aria-label="Photo of a vacuum floor tool gliding over a dark hardwood floor"></div>
  <svg class="silver-sweep" viewBox="0 0 360 556" aria-hidden="true">
    <defs>
      <linearGradient id="silverL" x1="0" y1="0" x2="0" y2="1">
        <stop offset="0" stop-color="#cfd0d2"/>
        <stop offset=".25" stop-color="#f4f4f5"/>
        <stop offset="1" stop-color="#ffffff"/>
      </linearGradient>
    </defs>
    <path d="M0,200 Q180,160 360,190 L360,556 L0,556 Z" fill="url(#silverL)"/>
  </svg>
  <h2 class="label label-simple">Simple</h2>
  <p class="copy copy-simple">Installation of the Pelm Ovra is simple. Pelm Ovra™ fits between two household wall studs on an interior wall space and can be generally be installed in less than an hour. Have an electrician hard wire or simply plug and play from any 110/120Volt outlet.</p>
  <h2 class="label label-convenience">Convenience</h2>
  <p class="copy copy-convenience">Debris is stored inside an allergy resistant bag which captures 99.4% of pollens, bacteria and other harmful debris. Accessible compartment makes bag changes easy as well as service.</p>
  <svg class="page-band" viewBox="0 0 360 70" aria-hidden="true">
    <path d="M0,30 Q180,10 360,22 L360,70 L0,70 Z" fill="var(--red)"/>
    <path d="M0,30 Q180,10 360,22" fill="none" stroke="#ffffff" stroke-width="3"/>
  </svg>
</section>

<section class="page spread-right" aria-label="Inside right page">
  <div class="photo unit-photo" role="img" aria-label="Photos of the wall-mounted vacuum unit with open bag compartment and hose docking station in a hallway"></div>
  <svg class="silver-sweep" viewBox="0 0 360 556" aria-hidden="true">
    <defs>
      <linearGradient id="silverR" x1="0" y1="0" x2="0" y2="1">
        <stop offset="0" stop-color="#bfc1c4"/>
        <stop offset=".3" stop-color="#eeeeef"/>
        <stop offset="1" stop-color="#ffffff"/>
      </linearGradient>
    </defs>
    <path d="M0,185 Q180,150 360,165 L360,556 L0,556 Z" fill="url(#silverR)"/>
  </svg>
  <div class="product-name"><span class="mark"></span>Pelm Ovra</div>
  <h2 class="label label-demand">On Demand</h2>
  <p class="copy copy-demand">Total control is at your fingertips with Pelm Ovra™. Want more hose? Simply push the “out” button… All done? A quick push of the “in” button will retract up to 45 feet of hose back into the hose docking station.</p>
  <p class="copy copy-vision">Imagine a system with abundant vacuum performance. A system with the versatility of a central vacuum. A system that automatically stores away the hose on demand with no effort. A system that makes vacuuming easier. Such a system that would do it ALL… Pelm Ovra™ by Swivo-Lux</p>
  <p class="copy specs">Suction 142”<br>Airwatts 500</p>
  <svg class="page-band" viewBox="0 0 360 70" aria-hidden="true">
    <path d="M0,22 Q180,10 360,30 L360,70 L0,70 Z" fill="var(--red)"/>
  </svg>
  <div class="brand-box"><span class="mark"></span>Swivo-Lux</div>
</section>

</body>
</html>
```